TALLIS AT DWELLINGS, LLC Webpage portfolio

I want to create a Website that allows my potential clients to browse my Skilled work via before and after photos. I want the website to enhance the work that I provide and potentially drive new business, or at least solidify my work.
I also do 3D CAD and Modeling of New Spaces and it would be nice to show some of that work from pencil design to 3D modeling, which I feel may help give me more clients.

The website needs to show a solid carpenter/company with the skills to get any project completed.

Types of Jobs - Custom Carpentry & Finishes, Kitchens, Baths, Basements, Decks, Porches, Whole House Renovation - Skilled Craftsmanship (Hardwood Flooring, Floor and Wall Tile) and much more...

Target Market(s)

Residential Home Renovation, Kitchen and Bath Renovation, Home Improvement

Industry/Entity Type

Residential Construction

Number of Pages Required

5+ page

Font styles to use
Sans Serif
Script

Requirements
Must have
• Similar to Rimvale.com, except for Tallis At Dwellings.
• Must be inviting.
• My Services Offered
• A way to reach me or contact me for estimates with some sort of Screening Questionare.
Nice to have
• Inviting Colors
Should not have
• Not sure at this time

```html
<!DOCTYPE html>
<html lang="en">
<head>
<meta charset="utf-8">
<title>Tallis At Dwellings</title>
<link href="https://fonts.googleapis.com/css2?family=Roboto:ital,wght@0,400;0,500;0,700;1,400&display=swap" rel="stylesheet">
<style>
:root{
  --brand:#1f5f80;
  --brand-dark:#174a66;
  --accent:#1ba1e2;
  --ink:#2b2b2b;
  --muted:#5a5a5a;
  --pale:#f1f3f5;
  --white:#fff;
  --navy:#17415e;
  --rule:#8fb6c9;
}
*{box-sizing:border-box;margin:0;padding:0}
html,body{width:797px;height:1200px;overflow:hidden}
body{position:relative;font-family:'Roboto',sans-serif;color:var(--ink);background:var(--white)}
.abs{position:absolute}

/* hero */
.hero{left:0;top:0;width:797px;height:362px;
  background:
    linear-gradient(115deg,rgba(255,255,255,0) 0%,rgba(255,255,255,0) 42%,rgba(255,255,255,.35) 52%,rgba(255,255,255,0) 62%),
    linear-gradient(180deg,#c9cbcd 0%,#e4e4e2 22%,#ecebe8 40%,#a9a39b 62%,#8d877f 75%,#cfcdc9 88%,#bdbab5 100%)}
.hero-shade{left:0;top:0;width:797px;height:44px;background:linear-gradient(180deg,rgba(50,60,70,.35),rgba(50,60,70,0));border-bottom:1px solid rgba(255,255,255,.4)}
.logo{left:34px;top:14px;font-weight:700;font-size:13px;color:var(--brand-dark);display:flex;align-items:center;gap:6px}
.logo .mark{width:11px;height:11px;background:var(--brand-dark)}
.nav{top:15px;font-size:11px;font-weight:500;color:var(--white);letter-spacing:.2px;text-shadow:0 0 3px rgba(0,0,0,.25)}
.btn{top:10px;height:22px;border-radius:11px;font-size:9px;display:flex;align-items:center;justify-content:center}
.btn-login{left:640px;width:42px;border:1px solid var(--white);color:var(--white)}
.btn-quote{left:685px;width:81px;background:var(--white);color:var(--ink);font-weight:500}

/* welcome */
.welcome{left:0;top:362px;width:797px;height:72px;background:var(--brand);color:var(--white);text-align:center}
.welcome h1{position:absolute;top:2px;width:100%;font-size:14.5px;font-weight:700}
.welcome .rule{position:absolute;left:34px;top:27px;width:728px;border-top:1px dashed rgba(255,255,255,.6)}
.welcome p{position:absolute;left:34px;top:41px;width:728px;font-size:8.6px;line-height:13px}

/* section heads */
.sec-title{width:797px;text-align:center;font-size:14.5px;font-weight:700;color:var(--ink)}
.sec-title span{color:var(--accent)}
.dotted{left:34px;width:728px;border-top:1px dashed var(--rule)}

.services{left:0;top:434px;width:797px;height:206px;background:linear-gradient(180deg,#eef1f3,#f3f5f6)}
.card{top:507px;width:168px;height:83px;box-shadow:0 1px 3px rgba(0,0,0,.15)}
.card-img{width:100%;height:100%}
.badge{top:491px;width:32px;height:32px;border-radius:50%;background:var(--brand-dark);display:flex;align-items:center;justify-content:center}
.card-label{top:577px;width:153px;height:28px;background:linear-gradient(180deg,#26698c,#17506f);color:var(--white);font-size:9.2px;font-weight:500;display:flex;align-items:center;justify-content:center;border-radius:2px;box-shadow:0 1px 2px rgba(0,0,0,.2)}

.shot{top:697px;height:124px}

.reviews{left:0;top:838px;width:797px;height:276px;background:var(--pale)}
.quote{font-size:8.2px;line-height:13px;font-style:italic;color:var(--muted)}
.quote.left{left:36px;width:270px;text-align:right}
.quote.right{left:490px;width:272px;text-align:left}
.who{font-size:8.5px;color:var(--ink)}
.avatar{width:51px;height:51px;border-radius:50%;background:radial-gradient(circle at 50% 45%,#d9c2b2 0%,#a88a76 55%,#4e4038 100%)}
.vline{left:398px;top:908px;height:146px;border-left:1px dashed var(--rule)}

.skyline{left:0;top:1064px;width:797px;height:50px;background:linear-gradient(180deg,rgba(23,65,94,0) 0%,rgba(23,65,94,.12) 55%,rgba(23,65,94,.45) 100%);border-bottom:2px solid var(--navy)}

/* footer */
.f-main{top:1147px;font-size:9px;font-weight:700;color:#333}
.f-rule{left:40px;top:1166px;width:592px;border-top:1px solid #e2e2e2}
.f-small{top:1175px;font-size:7.8px;color:#444}
.f-logo{left:672px;top:1133px;font-weight:700;font-size:11.5px;color:var(--brand-dark)}
.social{top:1172px;width:16px;height:16px;background:var(--brand-dark);border-radius:2px}
</style>
</head>
<body>

<header>
  <div class="abs hero" role="img" aria-label="Photo of a bright open-plan living room with grey sofas and a modern kitchen"></div>
  <div class="abs hero-shade"></div>
  <div class="abs logo"><span class="mark"></span>Tallis At Dwellings</div>
  <nav>
    <span class="abs nav" style="left:246px">HOME</span>
    <span class="abs nav" style="left:302px;opacity:.85">ABOUT</span>
    <span class="abs nav" style="left:361px;opacity:.85">SERVICES</span>
    <span class="abs nav" style="left:434px;opacity:.85">GALLERY</span>
    <span class="abs nav" style="left:504px;opacity:.85">CONTACT</span>
  </nav>
  <span class="abs btn btn-login">Log In</span>
  <span class="abs btn btn-quote">Request a Quote</span>
</header>

<section class="abs welcome">
  <h1>Welcome to Tallis At Dwellings</h1>
  <div class="rule"></div>
  <p>Sed ut perspiciatis unde omnis iste natus error sit voluptatem accusantium doloremque laudantium, totam rem aperiam, eaque ipsa quae ab illo chomu inventore veritatis et quasi architecto beatae vitae dicta sunt explicabo. Nemo enim ipsam voluptatem quia voluptas sit aspernatur aut odit aut fugit, sed quia consequun.</p>
</section>

<section class="abs services" role="presentation"></section>
<h2 class="abs sec-title" style="left:0;top:444px">Our <span>Services</span></h2>
<div class="abs dotted" style="top:470px"></div>

<div class="abs card" style="left:34px"><div class="card-img" role="img" aria-label="Photo of a large renovated family house with a lawn" style="background:linear-gradient(180deg,#3f6fc0 0%,#8eaedb 40%,#d8d2c4 58%,#7a8a5a 70%,#3f7a2c 100%)"></div></div>
<div class="abs card" style="left:221px"><div class="card-img" role="img" aria-label="Photo of a renovated kitchen with white cabinets" style="background:linear-gradient(180deg,#efeae0 0%,#d8cdb9 45%,#9b8466 75%,#6f5d48 100%)"></div></div>
<div class="abs card" style="left:408px"><div class="card-img" role="img" aria-label="Photo of a renovated bathroom with stone tile and dark vanity" style="background:linear-gradient(90deg,#c1a78c 0%,#a08670 45%,#5a4e46 70%,#2f2c2b 100%)"></div></div>
<div class="abs card" style="left:594px"><div class="card-img" role="img" aria-label="Photo of an empty room being painted with a ladder" style="background:linear-gradient(180deg,#f6ead8 0%,#e8cca8 55%,#c9996a 85%,#a87a4f 100%)"></div></div>

<div class="abs badge" style="left:102px"><svg width="16" height="16" viewBox="0 0 16 16" stroke="#fff" stroke-width="2" stroke-linecap="round"><path d="M3 3l10 10M13 3L3 13"/></svg></div>
<div class="abs badge" style="left:289px"><svg width="16" height="16" viewBox="0 0 16 16" fill="none" stroke="#fff" stroke-width="1.5"><rect x="2" y="6" width="12" height="8"/><path d="M2 9h12M8 6v8M5 2v3M11 2v3"/></svg></div>
<div class="abs badge" style="left:476px"><svg width="16" height="16" viewBox="0 0 16 16" fill="#fff"><rect x="2" y="3" width="10" height="5" rx="1"/><rect x="12" y="4.5" width="3" height="2"/><rect x="4" y="8" width="3" height="6"/></svg></div>
<div class="abs badge" style="left:662px"><svg width="16" height="16" viewBox="0 0 16 16" fill="none" stroke="#fff" stroke-width="1.6"><rect x="2" y="2" width="11" height="4" fill="#fff"/><path d="M13 4h1.5v4H8v2"/><rect x="7" y="10" width="2" height="5" fill="#fff"/></svg></div>

<div class="abs card-label" style="left:42px">Residential Home Renovations</div>
<div class="abs card-label" style="left:228px">Kitchen Renovations</div>
<div class="abs card-label" style="left:415px">Bath Renovations</div>
<div class="abs card-label" style="left:601px">Home Improvement</div>

<section class="projects">
  <h2 class="abs sec-title" style="left:0;top:652px">Latest <span>Projects</span></h2>
  <div class="abs dotted" style="top:678px"></div>
  <div class="abs shot" style="left:0;width:160px;background:linear-gradient(180deg,#e2ded6 0%,#c9bfb0 45%,#9c7d5c 75%,#6e4c2e 100%)" role="img" aria-label="Project photo of an empty renovated kitchen with wood floors"></div>
  <div class="abs shot" style="left:160px;width:159px;background:linear-gradient(180deg,#6d4a37 0%,#a9a49a 40%,#8e7a66 65%,#4d382b 100%)" role="img" aria-label="Project photo of a covered porch with a stone fireplace"></div>
  <div class="abs shot" style="left:319px;width:159px;background:linear-gradient(180deg,#4a3020 0%,#8a5a32 45%,#5c3b22 70%,#241811 100%)" role="img" aria-label="Project photo of a dark wood kitchen with pendant lights"></div>
  <div class="abs shot" style="left:478px;width:160px;background:linear-gradient(180deg,#3568b0 0%,#9fb4cf 30%,#c4c6c6 50%,#8f8d80 72%,#5f6b3e 100%)" role="img" aria-label="Project photo of a house exterior with new siding"></div>
  <div class="abs shot" style="left:638px;width:159px;background:linear-gradient(180deg,#eceae5 0%,#d6d2ca 45%,#a58f7c 70%,#7e8a5a 100%)" role="img" aria-label="Project photo of a front porch with white railings and stone column"></div>
</section>

<section class="abs reviews" role="presentation"></section>
<h2 class="abs sec-title" style="left:0;top:852px">What <span>People Say</span></h2>
<div class="abs dotted" style="top:878px"></div>
<div class="abs dotted" style="top:981px"></div>
<div class="abs vline"></div>

<p class="abs quote left" style="top:906px">Duis aute irure dolor in reprehenderit in voluptate velit esse cillum dolore eu fugiat nulla pariatur. Excepteur sint occaecat cupidatat non proident, sunt in culpa qui officia deserunt mollit.</p>
<p class="abs who" style="left:36px;width:270px;text-align:right;top:953px">Evan Marsh, Operations Manager</p>
<div class="abs avatar" style="left:326px;top:907px" role="img" aria-label="Portrait photo of the client"></div>

<div class="abs avatar" style="left:420px;top:907px" role="img" aria-label="Portrait photo of the client"></div>
<p class="abs quote right" style="top:906px">Provident, similique sunt in culpa qui officia deserunt mollitia animi, id est laborum et dolorum fuga. Et harum quidem rerum facilis est et expedita distinctio. Nam libero tempore, cum soluta nobis.</p>
<p class="abs who" style="left:490px;top:953px">Nora Vale, Creative Designer</p>

<p class="abs quote left" style="top:998px">Luis aute irure dolor in reprehenderit in piluptate velit esse cillum dolore eu fugiat nulla pariatur. Excepteur sint occaecat cupidatat non proident, sunt in culpa qui officia deserunt mollit.</p>
<p class="abs who" style="left:36px;width:270px;text-align:right;top:1045px">Ida Brook, Manager</p>
<div class="abs avatar" style="left:326px;top:999px" role="img" aria-label="Portrait photo of the client"></div>

<div class="abs avatar" style="left:420px;top:999px" role="img" aria-label="Portrait photo of the client"></div>
<p class="abs quote right" style="top:998px">At vero eos et accusamus et iusto odio dignissimos ducimus qui blanditiis praesentium voluptatum deleniti atque corrupti quos dolores et quas molestias excepturi sint occaecati asperiores.</p>
<p class="abs who" style="left:490px;top:1045px">Owen Pike, Developer</p>

<div class="abs skyline" role="img" aria-label="Illustration of a city skyline with an airport and planes"></div>

<footer>
  <svg class="abs" style="left:41px;top:1147px" width="10" height="10" viewBox="0 0 10 10" fill="none" stroke="#333" stroke-width="1.5"><circle cx="4" cy="4" r="3"/><path d="M6.3 6.3L9.5 9.5"/></svg>
  <span class="abs f-main" style="left:62px">Help &amp; Contact</span>
  <span class="abs f-main" style="left:140px">Home Renovation</span>
  <span class="abs f-main" style="left:228px">Kitchen Renovation</span>
  <span class="abs f-main" style="left:322px">Bath Renovation</span>
  <span class="abs f-main" style="left:406px">Home Improvement</span>
  <div class="abs f-rule"></div>
  <span class="abs f-small" style="left:41px">About</span>
  <span class="abs f-small" style="left:74px">Blog</span>
  <span class="abs f-small" style="left:102px">Gallery</span>
  <span class="abs f-small" style="left:137px">testimonials</span>
  <span class="abs f-small" style="left:192px">Public Policy</span>
  <span class="abs f-small" style="left:249px">Sitemap</span>
  <span class="abs f-small" style="left:290px">Partners</span>
  <span class="abs f-small" style="left:548px">© 2015–2017</span>
  <span class="abs f-small" style="left:608px">Privacy</span>
  <span class="abs f-small" style="left:646px">Legal</span>
  <span class="abs social" style="left:674px"></span>
  <span class="abs social" style="left:697px"></span>
  <span class="abs social" style="left:719px"></span>
  <span class="abs social" style="left:742px"></span>
  <div class="abs f-logo">Tallis At Dwellings</div>
</footer>

</body>
</html>
```